BrambleWorks business card

Looking for business card design that supports our company/software values. We have 2 logo designs at the moment but open to change if you think you can enhance the brand. Check out website www.brambleworks.com.au.

Target Market(s)

Education

Contact Information for Business Card

Name, title, mobile, email and website

Font styles to use
Sans Serif

Colors

Designer to choose colors to be used in the design.

Requirements
Must have
• BrambleWorks logo with tree and tagline on rear side with dark grey background colour

```html
<!DOCTYPE html>
<html lang="en">
<head>
<meta charset="utf-8">
<title>BrambleWorks business card</title>
<link href="https://fonts.googleapis.com/css2?family=Montserrat:wght@400;500;600&display=swap" rel="stylesheet">
<style>
  :root {
    --backdrop: #a9aaa9;
    --card-dark: #4f504f;
    --card-light: #ffffff;
    --accent: #f6b73c;
    --ink: #3a3a3a;
    --ink-soft: #555555;
    --wash-start: #ececec;
    --wash-end: #f4f6f1;
  }
  * { margin: 0; padding: 0; box-sizing: border-box; }
  html, body {
    width: 1200px; height: 930px; overflow: hidden;
    background: var(--backdrop);
    font-family: "Montserrat", sans-serif;
  }
  .canvas { position: relative; width: 1200px; height: 930px; }

  .card {
    position: absolute;
    width: 540px; height: 310px;
    border-radius: 22px;
    overflow: hidden;
  }

  /* Rear side */
  .card-back {
    left: 90px; top: 90px;
    background: var(--card-dark);
    display: flex; align-items: center; justify-content: center;
  }
  .back-brand {
    display: flex; align-items: center; gap: 14px;
    color: var(--card-light);
    font-weight: 600; font-size: 34px; letter-spacing: 0.5px;
  }
  .back-brand .dot {
    width: 26px; height: 26px; border-radius: 50%;
    background: var(--accent);
  }

  /* Front side */
  .card-front {
    left: 570px; top: 530px;
    background: var(--card-light);
  }
  .decoration {
    position: absolute; left: 200px; top: -10px;
    width: 330px; height: 300px;
    border-radius: 50%;
    background: radial-gradient(circle at 55% 45%, var(--wash-start) 0%, var(--wash-end) 60%, rgba(255,255,255,0) 72%);
  }
  .brand {
    position: absolute; left: 34px; top: 40px;
  }
  .brand-name {
    display: flex; align-items: center; gap: 8px;
    font-size: 26px; font-weight: 500; color: var(--ink);
    border-bottom: 1px solid var(--ink); padding-bottom: 3px;
  }
  .brand-name .dot {
    width: 14px; height: 14px; border-radius: 50%; background: var(--ink);
  }
  .brand-tagline {
    font-size: 11px; color: var(--ink-soft); margin-top: 3px; padding-left: 22px;
  }
  .person {
    position: absolute; right: 34px; top: 56px; text-align: right;
  }
  .person-name {
    font-size: 24px; font-weight: 500; color: var(--accent); letter-spacing: 1px;
  }
  .person-title { font-size: 14px; color: var(--ink); margin-top: 2px; }
  .rule-top {
    position: absolute; left: 260px; right: 34px; top: 126px;
    height: 1.5px; background: var(--accent);
  }
  .address {
    position: absolute; right: 34px; top: 150px; text-align: right;
    font-size: 15px; line-height: 1.45; color: var(--ink);
  }
  .rule-bottom {
    position: absolute; left: 34px; width: 300px; top: 210px;
    height: 1.5px; background: var(--accent);
  }
  .contacts {
    position: absolute; left: 34px; top: 222px;
    list-style: none; font-size: 15px; color: var(--ink); line-height: 1.55;
  }
  .contacts li { display: flex; align-items: center; gap: 9px; }
  .contacts svg { width: 12px; height: 12px; flex: none; }
</style>
</head>
<body>
<main class="canvas">

  <section class="card card-back" aria-label="Card rear side">
    <div class="back-brand"><span class="dot"></span>BrambleWorks</div>
  </section>

  <section class="card card-front" aria-label="Card front side">
    <div class="decoration" role="img" aria-label="Faint tree and figures decoration"></div>

    <div class="brand">
      <div class="brand-name"><span class="dot"></span>BrambleWorks</div>
      <div class="brand-tagline">Student Success Platform</div>
    </div>

    <div class="person">
      <div class="person-name">DANIEL HARPER</div>
      <div class="person-title">Director</div>
    </div>
    <div class="rule-top"></div>

    <address class="address" style="font-style:normal">
      1820 Alder Lane<br>Riverton, MO 65100
    </address>

    <div class="rule-bottom"></div>
    <ul class="contacts">
      <li>
        <svg viewBox="0 0 12 12"><path d="M2 1h2.5l1 3-1.5 1a6 6 0 0 0 3 3l1-1.5 3 1V11a1 1 0 0 1-1 1A10 10 0 0 1 1 2a1 1 0 0 1 1-1z" fill="#f6b73c"/></svg>
        555-014-2873
      </li>
      <li>
        <svg viewBox="0 0 12 12"><rect x="1" y="2.5" width="10" height="7" fill="none" stroke="#f6b73c" stroke-width="1.3"/><path d="M1 2.5l5 4 5-4" fill="none" stroke="#f6b73c" stroke-width="1.3"/></svg>
        info@brambleworks.com.au
      </li>
      <li>
        <svg viewBox="0 0 12 12"><circle cx="6" cy="6" r="5" fill="#f6b73c"/><path d="M1 6h10M6 1c-2 2.5-2 7.5 0 10M6 1c2 2.5 2 7.5 0 10" fill="none" stroke="#fff" stroke-width="0.8"/></svg>
        www.brambleworks.com.au
      </li>
    </ul>
  </section>

</main>
</body>
</html>
```